2022 Landscaping Services

Please use the prior year design as an example. Similar style but DO NOT COPY IT EXACTLY- you can use different photos from our website if you like. Same text for year 2022.
Design should clearly depict the differences between the 3 products so people can buy one of them. Be creative!

size 8.5" x 11"

Must provide source file in photoshop if you are winner

Requirements
Must have
• Same text as original flier but with year 2022

```html
<!DOCTYPE html>
<html lang="en">
<head>
<meta charset="utf-8">
<title>2022 Gravesite Landscaping Packages</title>
<link href="https://fonts.googleapis.com/css2?family=Barlow+Semi+Condensed:wght@400;500;600;700&family=Barlow+Condensed:wght@700&family=Montserrat:wght@500&family=Kaushan+Script&display=swap" rel="stylesheet">
<style>
  :root {
    --page-bg: #c4c5c7;
    --paper: #ffffff;
    --brand-red: #8a0d0d;
    --brand-red-dark: #6e0909;
    --footer-wine: #7b2335;
    --ink: #2b2b2b;
    --header-dark: #393939;
    --header-light: #e6e6e4;
    --row-shade: #f0f0f0;
    --divider: #e2e2e2;
    --ring-gray: #dadada;
    --photo-top: #cfc9c1;
    --photo-bottom: #a3ad93;
  }
  * { margin: 0; padding: 0; box-sizing: border-box; }
  html, body { width: 987px; height: 1200px; overflow: hidden; background: var(--page-bg); }
  body { font-family: "Barlow Semi Condensed", "Arial Narrow", sans-serif; color: var(--ink); }

  .flyer { position: absolute; left: 28px; top: 0; width: 930px; height: 1200px; background: var(--paper); overflow: hidden; }
  .abs { position: absolute; }

  .hero-art { position: absolute; left: 0; top: 0; width: 930px; height: 660px; }

  .brand { left: 40px; top: 30px; width: 190px; text-align: center; }
  .brand-mark { width: 76px; height: 76px; border: 2px solid #9a9a9a; border-radius: 50%; margin: 0 auto 16px; }
  .brand-name { font-weight: 600; font-size: 34px; line-height: 40px; color: var(--brand-red); text-transform: uppercase; letter-spacing: 0.5px; }

  .title-block { left: 48px; top: 300px; width: 340px; text-align: center; color: #fff; font-family: "Barlow Condensed", "Arial Narrow", sans-serif; font-weight: 700; }
  .title-year { font-size: 78px; line-height: 78px; }
  .title-line { font-size: 50px; line-height: 45px; }

  .badge { left: 722px; top: 534px; width: 96px; height: 96px; text-align: center; font-family: "Kaushan Script", cursive; font-size: 25px; line-height: 25px; color: #222; padding-top: 22px; }

  .pricing { left: 41px; top: 647px; width: 843px; height: 400px; }
  .col-rule { position: absolute; top: 71px; width: 5px; height: 329px; background: var(--divider); }
  .head { position: absolute; top: 0; height: 71px; display: flex; flex-direction: column; justify-content: center; text-transform: uppercase; font-weight: 600; line-height: 24px; }
  .head-services { left: 0; width: 219px; background: var(--header-dark); color: #fff; font-size: 33px; line-height: 29px; padding-left: 12px; }
  .head-plan { background: var(--header-light); color: var(--ink); text-align: center; font-size: 26px; }
  .head-plan.is-featured { background: var(--brand-red); color: #fff; font-size: 28px; }

  .row { position: absolute; left: 0; width: 843px; }
  .row.is-shaded { background: var(--row-shade); }
  .row-label { position: absolute; left: 11px; top: 50%; transform: translateY(-50%); font-size: 18.5px; font-weight: 600; line-height: 20px; }
  .cell { position: absolute; top: 50%; transform: translateY(-50%); text-align: center; }
  .cell-note { font-size: 12.5px; font-weight: 500; line-height: 15px; }
  .cell svg { width: 19px; height: 19px; display: block; margin: 0 auto; }

  .price { position: absolute; top: 1054px; text-align: center; }
  .price-amount { font-size: 27px; font-weight: 600; line-height: 30px; }
  .price-amount.is-featured { color: var(--brand-red); }
  .price-note { font-size: 11.5px; font-weight: 400; line-height: 15px; margin-top: 6px; }
  .term-row { display: flex; justify-content: space-between; font-size: 11.5px; margin-top: 5px; padding: 0 6px 0 2px; }

  .validity { left: 39px; top: 1083px; width: 111px; height: 58px; background: var(--header-dark); color: #fff; border-radius: 3px 3px 0 0; text-align: center; font-size: 14.5px; line-height: 18px; padding-top: 10px; }

  .footer { left: 0; top: 1141px; width: 930px; height: 59px; background: var(--footer-wine); color: #fff; font-family: "Montserrat", Arial, sans-serif; font-weight: 500; font-size: 18.5px; display: flex; align-items: center; justify-content: center; gap: 20px; }
  .footer-item { display: flex; align-items: center; gap: 8px; }
  .footer-item svg { width: 17px; height: 17px; }
</style>
</head>
<body>
<svg width="0" height="0" style="position:absolute">
  <defs>
    <symbol id="icon-tick" viewBox="0 0 24 24">
      <path d="M20 10.5A8.5 8.5 0 1 1 15.5 4" fill="none" stroke="#8a0d0d" stroke-width="2" stroke-linecap="round"/>
      <path d="M7.5 11.5l4 4 9-10" fill="none" stroke="#8a0d0d" stroke-width="2.2" stroke-linecap="round" stroke-linejoin="round"/>
    </symbol>
    <symbol id="icon-none" viewBox="0 0 24 24">
      <circle cx="12" cy="12" r="9" fill="none" stroke="#222" stroke-width="2.4"/>
      <path d="M6 18L18 6" stroke="#222" stroke-width="2.4"/>
    </symbol>
  </defs>
</svg>

<main class="flyer">
  <svg class="hero-art" viewBox="0 0 930 660">
    <defs>
      <clipPath id="photo-clip"><circle cx="691" cy="217" r="368"/></clipPath>
      <linearGradient id="photo-tone" x1="0" y1="0" x2="0" y2="1">
        <stop offset="0" stop-color="var(--photo-top)"/>
        <stop offset="1" stop-color="var(--photo-bottom)"/>
      </linearGradient>
      <radialGradient id="title-fill" cx="0.45" cy="0.35" r="0.7">
        <stop offset="0" stop-color="#950f0f"/>
        <stop offset="1" stop-color="#6e0909"/>
      </radialGradient>
    </defs>
    <circle cx="663" cy="201" r="417" fill="var(--ring-gray)"/>
    <circle cx="674" cy="208" r="395" fill="var(--brand-red)"/>
    <circle cx="691" cy="217" r="376" fill="var(--ring-gray)"/>
    <g role="img" aria-label="Photo of a cemetery in spring with blossoming trees, gravestones, shrubs and lawn">
      <rect x="0" y="0" width="930" height="660" fill="url(#photo-tone)" clip-path="url(#photo-clip)"/>
    </g>
    <circle cx="217" cy="415" r="190" fill="#fff"/>
    <circle cx="217" cy="415" r="186" fill="url(#title-fill)"/>
    <circle cx="217" cy="415" r="171" fill="none" stroke="#f2c9c9" stroke-width="2.4" stroke-linecap="round" stroke-dasharray="0.1 6"/>
    <circle cx="770" cy="582" r="49" fill="#cfcfcf" stroke="#fff" stroke-width="3"/>
    <path d="M760 628 L770 642 L780 628 Z" fill="#cfcfcf"/>
  </svg>

  <div class="abs brand">
    <div class="brand-mark"></div>
    <div class="brand-name">Maplewood<br>Cemetery</div>
  </div>

  <h1 class="abs title-block">
    <div class="title-year">2022</div>
    <div class="title-line">GRAVESITE</div>
    <div class="title-line">LANDSCAPING</div>
    <div class="title-line">PACKAGES</div>
  </h1>

  <div class="abs badge">Most<br>Popular</div>

  <section class="abs pricing">
    <div class="head head-services">Services<br>Offered</div>
    <div class="head head-plan" style="left:225px;width:184px">Sasonal Care<br>Endowment</div>
    <div class="head head-plan" style="left:418px;width:189px">Basic Care<br>Endowment</div>
    <div class="head head-plan is-featured" style="left:615px;width:228px">Perpetual Care<br>Endowment</div>

    <div class="row is-shaded" style="top:79px;height:58px">
      <div class="row-label">Weeding &amp; Trimming on<br>Your GravesIte</div>
      <div class="cell cell-note" style="left:225px;width:184px">Approximately every 7 weeks<br>during the growing season:<br>Mid-April through Mid-October</div>
      <div class="cell cell-note" style="left:418px;width:189px">2 times per year:<br>Mid_May &amp; Mid-September<br>&nbsp;</div>
      <div class="cell cell-note" style="left:615px;width:228px">Approximately every 7 weeks<br>during the growing season:<br>Mid-April through Mid-October</div>
    </div>

    <div class="row" style="top:138px;height:54px">
      <div class="row-label">Payment Ensured<br>Forever Grave Care</div>
      <div class="cell" style="left:225px;width:184px"><svg><use href="#icon-none"/></svg></div>
      <div class="cell" style="left:418px;width:189px"><svg><use href="#icon-tick"/></svg></div>
      <div class="cell" style="left:615px;width:228px"><svg><use href="#icon-tick"/></svg></div>
    </div>

    <div class="row is-shaded" style="top:192px;height:37px">
      <div class="row-label">Monument Leveling</div>
      <div class="cell" style="left:225px;width:184px"><svg><use href="#icon-none"/></svg></div>
      <div class="cell" style="left:418px;width:189px"><svg><use href="#icon-tick"/></svg></div>
      <div class="cell" style="left:615px;width:228px"><svg><use href="#icon-tick"/></svg></div>
    </div>

    <div class="row" style="top:229px;height:42px">
      <div class="row-label">Monument Cleaning</div>
      <div class="cell" style="left:225px;width:184px"><svg><use href="#icon-none"/></svg></div>
      <div class="cell" style="left:418px;width:189px"><svg><use href="#icon-none"/></svg></div>
      <div class="cell" style="left:615px;width:228px"><svg><use href="#icon-tick"/></svg></div>
    </div>

    <div class="row is-shaded" style="top:271px;height:47px">
      <div class="row-label">Full Bed of Boxwood<br>Shrubs</div>
      <div class="cell" style="left:225px;width:184px"><svg><use href="#icon-none"/></svg></div>
      <div class="cell" style="left:418px;width:189px"><svg><use href="#icon-none"/></svg></div>
      <div class="cell" style="left:615px;width:228px"><svg><use href="#icon-tick"/></svg></div>
    </div>

    <div class="row" style="top:318px;height:46px">
      <div class="row-label">Replacement of Shrubs</div>
      <div class="cell" style="left:225px;width:184px"><svg><use href="#icon-none"/></svg></div>
      <div class="cell" style="left:418px;width:189px"><svg><use href="#icon-none"/></svg></div>
      <div class="cell" style="left:615px;width:228px"><svg><use href="#icon-tick"/></svg></div>
    </div>

    <div class="row is-shaded" style="top:364px;height:36px">
      <div class="row-label">Trust Certificate</div>
      <div class="cell" style="left:225px;width:184px"><svg><use href="#icon-none"/></svg></div>
      <div class="cell" style="left:418px;width:189px"><svg><use href="#icon-none"/></svg></div>
      <div class="cell" style="left:615px;width:228px"><svg><use href="#icon-tick"/></svg></div>
    </div>

    <div class="col-rule" style="left:411px"></div>
    <div class="col-rule" style="left:608px"></div>
  </section>

  <div class="price" style="left:263px;width:184px">
    <div class="price-amount">$357 | $238 | $119</div>
    <div class="term-row"><span>3 Years</span><span>2 Years</span><span>1 Years</span></div>
  </div>
  <div class="price" style="left:449px;width:217px">
    <div class="price-amount">$255</div>
    <div class="price-note">12 Monthly payments.<br>Call for single payment discounts.</div>
  </div>
  <div class="price" style="left:656px;width:232px">
    <div class="price-amount is-featured">$313</div>
    <div class="price-note">12 Monthly payments.<br>Call for single payment discounts.</div>
  </div>

  <div class="abs validity">Valid through<br>10/31/22</div>

  <footer class="abs footer">
    <span class="footer-item">
      <svg viewBox="0 0 24 24" fill="none" stroke="#fff" stroke-width="1.5"><path d="M12 21s-6-6.5-6-11a6 6 0 0 1 12 0c0 4.5-6 11-6 11z"/><circle cx="12" cy="10" r="2.2"/><path d="M4 21h16"/></svg>
      48 Elm Ave., Fairview, NJ 07022
    </span>
    <span class="footer-item">
      <svg viewBox="0 0 24 24" fill="none" stroke="#fff" stroke-width="1.5"><path d="M5 4h4l2 5-2.5 1.5a11 11 0 0 0 5 5L15 13l5 2v4a2 2 0 0 1-2 2A16 16 0 0 1 3 6a2 2 0 0 1 2-2z"/></svg>
      (201) 555-0148
    </span>
    <span class="footer-item">
      <svg viewBox="0 0 24 24" fill="none" stroke="#fff" stroke-width="1.5"><circle cx="12" cy="12" r="9"/><path d="M3 12h18M12 3c3 3 3 15 0 18M12 3c-3 3-3 15 0 18"/></svg>
      www.maplewoodcemetery.org
    </span>
  </footer>
</main>
</body>
</html>
```